Design a Pull Up Banner for Finance Broker Business

Pull up banner design. Dimensions 850 x 2000 mm for finance broker . Vertical standing banner will be on display at open homes, auctions and trade shows. Want it to match coporate colours, included logo and look cheerful / breezy with relevant images/ theme for housing / home ownership. Include contact details and text stating Name "Brightvale Financial Solutions" with something like "helping you achieve your financial goals". Include contact number 1300 42 63 51
website address www.brightvale.com.au
email info@brightvale.com.au
Target Market(s)
People seeking finance for home purchases, investment properties, asset finance - motor vehicles and business finance
Industry/Entity Type
Business
Requirements
Must have
- Business Name
- Contact number 1300 42 63 51
- email address info@brightvale.com.au
- Point form of what I do
Nice to have
- Catchy title about the service I provide
- Cheerful image - that match colours of business on website / logo
Should not have
- Too squashy

```html
<!DOCTYPE html>
<html lang="en">
<head>
<meta charset="utf-8">
<title>Brightvale Financial Solutions – Pull Up Banner</title>
<link rel="stylesheet" href="https://fonts.googleapis.com/css2?family=Montserrat:wght@500;600;700&display=swap">
<style>
  :root {
    --page-bg: #e6e8eb;
    --banner-white: #ffffff;
    --navy-dark: #1f2530;
    --brand-blue: #1a4f9f;
    --bright-blue: #3d8ff0;
    --swoosh-grey: #9aa1aa;
    --ink: #1a1d24;
    --logo-ink: #1c2230;
  }
  * { margin: 0; padding: 0; box-sizing: border-box; }
  html, body {
    width: 1200px; height: 1000px; overflow: hidden;
    background: var(--page-bg);
    font-family: "Montserrat", Arial, sans-serif;
  }
  .canvas { position: relative; width: 1200px; height: 1000px; }
  .banner {
    position: absolute; left: 419px; top: 45px;
    width: 362px; height: 910px;
    background: var(--navy-dark);
    overflow: hidden;
    box-shadow: 0 6px 24px rgba(0,0,0,0.18);
  }
  .hero-photo {
    position: absolute; left: 0; top: 120px; width: 362px; height: 450px;
    background:
      radial-gradient(ellipse 120px 150px at 110px 230px, rgba(214,170,150,0.55), transparent 70%),
      radial-gradient(ellipse 140px 170px at 250px 250px, rgba(150,185,220,0.6), transparent 70%),
      radial-gradient(ellipse 160px 90px at 290px 110px, rgba(235,225,205,0.7), transparent 70%),
      linear-gradient(180deg, #cfdbe8 0%, #bfc8d0 25%, #8a9bb2 55%, #3f495b 82%, var(--navy-dark) 100%);
  }
  .banner-shapes { position: absolute; inset: 0; width: 362px; height: 910px; }
  .brand-name {
    position: absolute; top: 58px; left: 0; width: 100%;
    text-align: center; color: var(--logo-ink); font-weight: 600;
  }
  .brand-name .name { display: block; font-size: 31px; letter-spacing: 1px; line-height: 1; }
  .brand-name .sub { display: block; font-size: 12.5px; margin-top: 7px; letter-spacing: 0.3px; }
  .service-list {
    position: absolute; top: 452px; left: 22px; width: 318px;
    list-style: none; display: grid; grid-template-columns: 1fr 1fr; gap: 8px 10px;
    color: #ffffff; font-size: 12.5px; font-weight: 600; line-height: 16px;
  }
  .service-list li { display: flex; align-items: center; gap: 6px; }
  .service-list svg { flex: none; width: 14px; height: 14px; }
  .headline {
    position: absolute; top: 557px; left: 0; width: 100%;
    text-align: center; font-weight: 700; font-size: 35px; line-height: 35px;
    text-transform: uppercase; letter-spacing: 0.5px;
  }
  .headline .accent { color: var(--bright-blue); display: block; }
  .headline .plain { color: #ffffff; display: block; }
  .headline-rule {
    position: absolute; top: 671px; left: 44px; width: 274px; height: 1px;
    background: rgba(255,255,255,0.7);
  }
  .tagline {
    position: absolute; top: 680px; left: 0; width: 100%;
    text-align: center; color: #ffffff; font-weight: 500; font-size: 18px; line-height: 25px;
  }
  .contact {
    position: absolute; top: 812px; left: 0; width: 100%; text-align: center; color: var(--ink);
  }
  .contact .phone { font-size: 28px; font-weight: 700; color: var(--brand-blue); line-height: 34px; letter-spacing: 0.5px; }
  .contact .email { font-size: 16px; font-weight: 500; line-height: 21px; }
  .contact .web { font-size: 16px; font-weight: 700; line-height: 22px; }
  .contact .web .domain { color: var(--brand-blue); }
</style>
</head>
<body>
<div class="canvas">
  <section class="banner">
    <div class="hero-photo" role="img" aria-label="Photo of a smiling young couple holding up house keys in front of a new home"></div>

    <svg class="banner-shapes" viewBox="0 0 362 910" aria-hidden="true">
      <path d="M0 0 H362 V115 C280 160 130 182 0 175 Z" fill="var(--banner-white)"/>
      <path d="M0 175 C130 182 280 160 362 115 V133 C280 176 130 198 0 190 Z" fill="var(--brand-blue)"/>
      <path d="M0 800 C110 775 250 758 362 760 V766 C250 764 110 781 0 808 Z" fill="var(--swoosh-grey)"/>
      <path d="M0 808 C110 781 250 764 362 766 V785 C250 782 110 800 0 830 Z" fill="var(--brand-blue)"/>
      <path d="M0 830 C110 800 250 782 362 785 V910 H0 Z" fill="var(--banner-white)"/>
    </svg>

    <div class="brand-name">
      <span class="name">BRIGHTVALE</span>
      <span class="sub">FINANCIAL SOLUTIONS PTY LTD</span>
    </div>

    <ul class="service-list">
      <li><svg viewBox="0 0 14 14"><circle cx="7" cy="7" r="7" fill="var(--bright-blue)"/><path d="M3.8 7.2 L6 9.3 L10.3 4.8" fill="none" stroke="#fff" stroke-width="1.8"/></svg>Home Loans</li>
      <li><svg viewBox="0 0 14 14"><circle cx="7" cy="7" r="7" fill="var(--bright-blue)"/><path d="M3.8 7.2 L6 9.3 L10.3 4.8" fill="none" stroke="#fff" stroke-width="1.8"/></svg>Investment Property</li>
      <li><svg viewBox="0 0 14 14"><circle cx="7" cy="7" r="7" fill="var(--bright-blue)"/><path d="M3.8 7.2 L6 9.3 L10.3 4.8" fill="none" stroke="#fff" stroke-width="1.8"/></svg>Vehicle &amp; Asset Finance</li>
      <li><svg viewBox="0 0 14 14"><circle cx="7" cy="7" r="7" fill="var(--bright-blue)"/><path d="M3.8 7.2 L6 9.3 L10.3 4.8" fill="none" stroke="#fff" stroke-width="1.8"/></svg>Business Finance</li>
    </ul>

    <h1 class="headline">
      <span class="accent">Brightvale</span>
      <span class="plain">Financial</span>
      <span class="accent">Solutions</span>
    </h1>
    <div class="headline-rule"></div>
    <p class="tagline">Helping you achieve your<br>Financial Goals</p>

    <div class="contact">
      <div class="phone">1300 42 63 51</div>
      <div class="email">info@brightvale.com.au</div>
      <div class="web">www.<span class="domain">brightvale</span>.com.au</div>
    </div>
  </section>
</div>
</body>
</html>
```